Web Design Project

I'm looking for a major redesign for my existing photographic art website: www.brightmeadowart.com. Here are my complaints about the current layout: 1) It looks unsophisticated (we will, of course, delete the "sale" banner; 2) the images are vastly too small when displayed in the gallery; 3) I'm not wild about the navigation; 4) the Flash has got to go; 4) there has to be an easy way to significantly enlarge the photos for viewing; 5) the copy is a bit over the top - we will be rewriting it. Other than that, it's a good site :)

The market for the photography is principally commercial applications - interior designers, etc. who are concerned with how these images will look in hospitals, office buildings, etc. The leading competitor in this space has a much better site: www.walterpriske.com. Another site worth viewing is: www.torvelt.com. This site is much more akin to my site.

We will be reducing the number of photos available. Total count will be approximately 400. The largest collection will be the "petal study" - close up photography of flowers, plants, etc.

I am amazed at the quality of the submissions - which has made the selection process very, very difficult. Each of you should be very proud of the quality of work you produce. Beyond this web-site, which is a "sideline" for me, I run a large marketing organization....and have shared these submissions with all of my colleagues who were duly impressed. Hopefully we will have an opportunity to work with you on a differentp project!

Thank you!!!
Mark

```html
<!DOCTYPE html>
<html lang="en">
<head>
<meta charset="utf-8">
<title>Bright Meadow – Photography by Mark Halvorsen</title>
<link href="https://fonts.googleapis.com/css2?family=Marcellus&family=PT+Sans:wght@400;700&family=PT+Sans+Narrow&display=swap" rel="stylesheet">
<style>
:root{
  --frame:#1d1d20;
  --page-top:#2a2a31;
  --page-mid:#3a3a44;
  --page-low:#141418;
  --panel-line:#6d6d74;
  --lime:#c6d92e;
  --text:#ffffff;
  --muted:#c9c9cf;
  --field:#ffffff;
}
*{box-sizing:border-box;margin:0;padding:0}
html,body{width:1200px;height:938px;overflow:hidden;background:var(--frame)}
.page{
  position:absolute;left:6px;top:6px;width:1188px;height:926px;
  background:linear-gradient(180deg,var(--page-top) 0%,var(--page-mid) 38%,#2b2b33 55%,var(--page-low) 100%);
  font-family:Arial,"PT Sans",sans-serif;color:var(--text);
}
.brand{position:absolute;left:42px;top:69px;display:flex;align-items:center;gap:12px}
.brand-mark{width:72px;height:72px;background:#000;border:1px solid #777}
.brand-name{font-family:"PT Sans",sans-serif;font-weight:700;font-size:40px;color:var(--text);letter-spacing:-.5px}
.account{position:absolute;right:280px;top:66px;font-size:13px;line-height:30px;color:var(--text);white-space:nowrap}
.account a{color:var(--text);text-decoration:none}
.search{position:absolute;left:916px;top:60px;display:flex;gap:3px}
.search-field{width:163px;height:30px;background:var(--field);border:1px solid #999;font-size:12px;color:#888;padding:7px 6px}
.search-btn{width:63px;height:30px;background:var(--lime);color:#111;font-weight:700;font-size:14px;display:flex;align-items:center;justify-content:center}
.nav{position:absolute;right:43px;top:156px;display:flex;font-family:"PT Sans Narrow",sans-serif;font-size:17px;letter-spacing:.3px;white-space:nowrap}
.nav a{color:#e4e4e8;text-decoration:none}
.nav a.active{color:var(--lime)}
.nav .sep{margin:0 26px;color:#cfcfd4}
.hero{position:absolute;left:43px;top:186px;width:1106px;height:442px;border:1px solid var(--panel-line);display:flex}
.intro{width:443px;height:100%;border-right:1px solid var(--panel-line);
  background:linear-gradient(90deg,rgba(0,0,0,.55),rgba(20,20,24,.85) 60%,rgba(30,30,34,.6));padding:26px 30px 0 24px}
.intro h1{font-family:"Marcellus",serif;font-weight:400;font-size:47px;color:var(--lime);line-height:1;letter-spacing:1px}
.intro h2{font-family:"Marcellus",serif;font-weight:400;font-size:19px;color:var(--lime);margin-top:2px}
.intro p{font-size:14.6px;line-height:25px;text-align:justify;margin-top:24px;color:var(--text)}
.intro p + p{margin-top:24px}
.feature{position:relative;flex:1}
.feature-photo{position:absolute;inset:0;
  background:linear-gradient(180deg,#d9c3a3 0%,#c9b59a 22%,#6f8a46 45%,#2f5a1c 70%,#4d7a22 100%)}
.caption{position:absolute;left:0;right:0;bottom:0;height:65px;background:rgba(10,20,8,.6);border-top:1px solid var(--panel-line);
  font-family:"PT Sans",sans-serif;font-size:21px;line-height:24px;padding:8px 16px}
.strip{position:absolute;left:43px;top:628px;width:1106px;height:195px;border:1px solid var(--panel-line);border-top:none;
  background:linear-gradient(180deg,#2c2c32,#1e1e23)}
.thumb{position:absolute;top:17px;height:158px;border:1px solid #bdbdc2}
.t1{left:72px;width:230px;background:linear-gradient(180deg,#3d4a31,#cfd5d6 55%,#3b3a2f)}
.t2{left:320px;width:225px;background:linear-gradient(160deg,#1a0f20,#7a3a8e 50%,#1a0f20)}
.t3{left:564px;width:228px;background:linear-gradient(180deg,#b8b3a3,#8b7f68 45%,#6f6b4f)}
.t4{left:811px;width:231px;background:linear-gradient(180deg,#7aa0d0,#b8bcbf 30%,#6b6f63 60%,#3f4a35)}
.arrow{position:absolute;top:53px;width:52px;height:52px}
.arrow.prev{left:4px}
.arrow.next{right:4px}
.footer-nav{position:absolute;left:43px;top:844px;font-size:13px;color:var(--muted)}
.footer-nav a{color:var(--muted);text-decoration:none}
.copyright{position:absolute;right:39px;top:843px;font-size:13px;color:#a4a4aa}
</style>
</head>
<body>
<div class="page">
  <div class="brand"><div class="brand-mark"></div><span class="brand-name">Bright Meadow</span></div>

  <div class="account"><a href="#">My Account</a> | <a href="#">View Cart</a> | <a href="#">Chckout</a> | <a href="#">Log In</a> | <a href="#">Sign Up</a></div>
  <div class="search"><div class="search-field">Find a Photo</div><div class="search-btn">Search</div></div>

  <nav class="nav">
    <a class="active" href="#">HOME</a><span class="sep">/</span>
    <a href="#">GALLERY</a><span class="sep">/</span>
    <a href="#">ARCHITECTS/DESIGNERS</a><span class="sep">/</span>
    <a href="#">ABOUT THE ARTIST</a><span class="sep">/</span>
    <a href="#">ORDERING INFORMATION</a><span class="sep">/</span>
    <a href="#">CONTACT US</a>
  </nav>

  <section class="hero">
    <div class="intro">
      <h1>WELCOME</h1>
      <h2>to the world of Mark Halvorsen</h2>
      <p>Come in and enjoy a place where stunning horizons meet glorious skies. A place where light and shade dance together in flawless rhythm. Come in and discover a world of photography that begins and ends with a shutter. Come in, relax and browse the gallery. You are about to experience some of the most inspiring and enchanting imagery the world has to offer.</p>
      <p>Come in and enjoy a place where stunning horizons meet glorious skies. A place where light and shade dance together in flawless rhythm.</p>
    </div>
    <div class="feature">
      <div class="feature-photo" role="img" aria-label="Vine-covered pergola in a green garden under a sunset sky"></div>
      <div class="caption">Photography Mark Halvorsen.Photography that transcends our normal view of the world.</div>
    </div>
  </section>

  <section class="strip">
    <svg class="arrow prev" viewBox="0 0 52 52" aria-label="Previous">
      <circle cx="26" cy="26" r="25" fill="#4a4a50" stroke="#2a2a2e"/>
      <path d="M30 15 L19 26 L30 37" fill="none" stroke="#1f1f23" stroke-width="6"/>
    </svg>
    <div class="thumb t1" role="img" aria-label="Waterfall cascading over rocks in a forest"></div>
    <div class="thumb t2" role="img" aria-label="Close-up of a purple flower on a dark background"></div>
    <div class="thumb t3" role="img" aria-label="Domed stone church in a rolling countryside"></div>
    <div class="thumb t4" role="img" aria-label="Mountain valley under a blue sky"></div>
    <svg class="arrow next" viewBox="0 0 52 52" aria-label="Next">
      <circle cx="26" cy="26" r="25" fill="#4a4a50" stroke="#2a2a2e"/>
      <path d="M22 15 L33 26 L22 37" fill="none" stroke="#1f1f23" stroke-width="6"/>
    </svg>
  </section>

  <div class="footer-nav"><a href="#">Home</a> | <a href="#">Gallery</a> &nbsp;| <a href="#">Architects/Designers</a> | &nbsp;<a href="#">About The Artist</a> | <a href="#">Ordering Information</a> | <a href="#">Contact Us</a></div>
  <div class="copyright">© 2012 Halvorsen Photography</div>
</div>
</body>
</html>
```